5 Email Newsletter Templates Needed

We need 5 email templates for our email marketing campaign. We are an Insurance Agency in Los Angeles called KPT-Silverbrook Insurance Services. We use Mailvance Hub as our email marketing platform. The templates need to be simple, a nice header, not to busy and you will need to use our color palette. The first email template we need is for our current clients / prospects. The content we will put in this email will be insurance tips and information, short and simple about 2 small paragraphs. The next 3 templates all need to be the same but different colors. One red, one yellow and one green. These will be alerts from kpt-silverbrook. An example a major earthquake hits we will send a red alert. A legislative change on healthcare and we send a yellow alert. We buy another location and we send a green alert. The last email is for our COINs (Centers of Influence, the people who refer business to us). I uploaded an email from one of our business consultants to give an idea of the size and sophistication we are looking for. I also uploaded our corporate brochure and color palette so you can learn more about our firm.

Target Market(s)

Our target markets are commercial business 1mm plus in revenue, 500 employees, high net worth individuals. Our COINs are CPAs, CFOs, Business Managers

Requirements
Nice to have
• HTML Code is desired. You can also provide just an image file for the header and our email marketing program will do the coding for us.
Should not have
• No cartoon looking graphics. Do not use old-style fonts like Times New Roman.

```html
<!DOCTYPE html>
<html lang="en">
<head>
<meta charset="utf-8">
<title>KPT-Silverbrook Yellow Alert</title>
<link href="https://fonts.googleapis.com/css2?family=Arimo:wght@400;700&display=swap" rel="stylesheet">
<style>
  :root {
    --alert-yellow: #f4b900;
    --card-white: #ffffff;
    --footer-grey: #d3d3d3;
    --brand-teal: #0d4f55;
    --heading-red: #cc1f1f;
    --tip-blue: #1a5e8c;
    --text-dark: #111111;
    --text-grey: #3d3d3d;
    --rule-grey: #c9c9c9;
  }
  * { box-sizing: border-box; margin: 0; padding: 0; }
  html, body {
    width: 1013px; height: 1200px; overflow: hidden;
    background: var(--alert-yellow);
    font-family: "Arimo", Helvetica, Arial, sans-serif;
    color: var(--text-dark);
  }
  .browser-link {
    position: absolute; top: 66px; left: 0; width: 1013px;
    text-align: center; font-size: 10.5px; color: #fff;
  }
  .newsletter {
    position: absolute; left: 175px; top: 85px; width: 665px; height: 959px;
    background: var(--card-white); border-radius: 16px; overflow: hidden;
  }
  .masthead { position: absolute; left: 0; top: 0; width: 665px; height: 144px; border-bottom: 1px solid var(--alert-yellow); }
  .brand { position: absolute; left: 26px; top: 78px; display: flex; align-items: center; gap: 8px; }
  .brand-mark { width: 20px; height: 20px; background: var(--brand-teal); }
  .brand-name { font-size: 16px; font-weight: 700; color: var(--brand-teal); line-height: 1.2; letter-spacing: 0.5px; }
  .alert-title { position: absolute; right: 26px; top: 57px; font-size: 23px; font-weight: 700; color: var(--alert-yellow); line-height: 1; }
  .alert-subject { position: absolute; right: 26px; top: 93px; width: 165px; text-align: right; font-size: 14px; font-weight: 700; color: var(--text-grey); line-height: 15px; }

  .section-head {
    position: absolute; font-size: 15.5px; font-weight: 400; color: var(--heading-red);
    padding-left: 15px; height: 34px; border-bottom: 1px solid var(--rule-grey); line-height: 1;
  }
  .section-head svg { position: absolute; left: 0; top: 1px; }
  .main-head { left: 12px; top: 167px; width: 408px; }
  .tips-head { left: 442px; top: 167px; width: 197px; }

  .body-copy { font-size: 12.5px; line-height: 17.3px; hyphens: auto; -webkit-hyphens: auto; }
  .feature-image {
    position: absolute; left: 26px; top: 216px; width: 183px; height: 181px;
    background: radial-gradient(circle at 50% 45%, #7fd0ff 0%, #1a72c9 35%, #0b2f6e 75%, #061a40 100%);
  }
  .feature-title { position: absolute; left: 236px; top: 215px; width: 180px; font-size: 14px; font-weight: 700; color: var(--text-grey); line-height: 15px; }
  .feature-intro { position: absolute; left: 236px; top: 262px; width: 184px; }
  .feature-body { position: absolute; left: 26px; top: 424px; width: 386px; }
  .divider { position: absolute; left: 12px; top: 580px; width: 407px; height: 1px; background: var(--rule-grey); }
  .sub-head { position: absolute; left: 26px; top: 598px; font-size: 13.5px; font-weight: 700; color: var(--tip-blue); }
  .commercial-body { position: absolute; left: 26px; top: 636px; width: 386px; }

  .tip { position: absolute; left: 442px; width: 197px; padding-left: 14px; }
  .tip-title { font-size: 12.5px; font-weight: 700; color: var(--tip-blue); line-height: 14.5px; margin-bottom: 9px; }
  .tip-text { font-size: 12.5px; line-height: 14.4px; hyphens: auto; -webkit-hyphens: auto; }
  .tip-one { top: 215px; }
  .tip-two { top: 408px; }
  .tip-three { top: 595px; }
  .tip-rule { position: absolute; left: 442px; width: 197px; height: 1px; background: var(--rule-grey); }
  .rule-one { top: 398px; }
  .rule-two { top: 580px; }

  .footer { position: absolute; left: 0; top: 797px; width: 665px; height: 162px; background: var(--footer-grey); font-size: 11.5px; }
  .contact { position: absolute; left: 27px; top: 25px; line-height: 14.5px; }
  .contact p + p { margin-top: 14px; }
  .follow { position: absolute; right: 25px; top: 17px; display: flex; align-items: center; gap: 12px; font-size: 10px; }
  .social-icon { width: 23px; height: 23px; border-radius: 3px; }
  .social-one { background: #3b5b9a; }
  .social-two { background: #7fc6ea; }
  .footer-links { position: absolute; right: 28px; top: 129px; font-size: 10px; }
  .footer-links a { color: var(--text-dark); }
</style>
</head>
<body>
  <p class="browser-link">Having trouble reading this newsletter? Click here to view this in a browser.</p>

  <main class="newsletter">
    <header class="masthead">
      <div class="brand">
        <span class="brand-mark"></span>
        <span class="brand-name">KPT-SILVERBROOK<br>INSURANCE SERVICES</span>
      </div>
      <h1 class="alert-title">YELLOW ALERT!</h1>
      <p class="alert-subject">Legislative change on health care</p>
    </header>

    <h2 class="section-head main-head"><svg width="9" height="14" viewBox="0 0 9 14"><path d="M1 1 L7 7 L1 13" fill="none" stroke="#cc1f1f" stroke-width="1.2"/></svg>BUILDING THE FUTURE. TOGETHER.</h2>

    <div class="feature-image" role="img" aria-label="Medical caduceus symbol glowing on a blue background"></div>
    <h3 class="feature-title">Legislative change on health care</h3>
    <p class="body-copy feature-intro">consectetuer adipiscing elit, sed diam nonummy nibh euismod tincidLorem ipsum dolor sit amet, consectetuer adipiscing elit, sed diam nonummy nibh euismod tincidunt ut laoreet dolore magna aliquam erat volutpat. Ut wisi enim ad minim veniam, quis nostrud exerci</p>
    <p class="body-copy feature-body">Lorem ipsum dolor sit amet, consectetuer adipiscing elit, sed diam nonummy nibh euismod tincidLorem ipsum dolor sit amet, consectetuer adipiscing elit, sed diam nonummy nibh euismod tincidunt ut laoreet dolore magna aliquam erat volutpat. Ut wisi enim ad minim veniam, quis nostrud exerci tation ullamcorper suscipit lobortis nisl ut utem d exerci tation ullamcorper suscipit lobortis nisl ut aliquip ex ea commodo consequat. Duis aut vel eum iriure dolor in hendrerit in vulputate velit esse molestie consequat.</p>

    <div class="divider"></div>
    <h3 class="sub-head">COMMERCIAL INSURANCE</h3>
    <p class="body-copy commercial-body">Lorem ipsum dolor sit amet, consectetuer adipiscing elit, sed diam nonummy nibh euismod tincidLorem ipsum dolor sit amet, consectetuer adipiscing elit, sed diam nonummy nibh euismod tincidunt ut laoreet dolore magna aliquam erat volutpat. Ut wisi enim ad minim veniam, quis nostrud exerci tation ullamcorper suscipit lobortis nisl ut suscipit lobortis nisl ut aliquip ex ea commodo consequat. Duis autem san et iusto odio dignissim qui blandit praesent luptatum zzril delenit augue duis dolore te feugait nulla facilisi.</p>

    <h2 class="section-head tips-head"><svg width="9" height="14" viewBox="0 0 9 14"><path d="M1 1 L7 7 L1 13" fill="none" stroke="#cc1f1f" stroke-width="1.2"/></svg>INSURANCE TIPS</h2>

    <section class="tip tip-one">
      <h4 class="tip-title">Know your state's auto insurance requirements:</h4>
      <p class="tip-text">Most states require you to carry a minimum amount of liability coverage. Many states have "no-fault" auto insurance systems. Coverage for medical costs for you and your passengers is optional in some states. Coverage for damage to your car is optional.</p>
    </section>
    <div class="tip-rule rule-one"></div>
    <section class="tip tip-two">
      <h4 class="tip-title">Write up your personal auto insurance profile:</h4>
      <p class="tip-text">List pertinent information concerning what type of vehicle you drive, where you drive, who else drives, what your driving record is, where you live, what optional safety features your car has. This profile will make the next step easier.</p>
    </section>
    <div class="tip-rule rule-two"></div>
    <section class="tip tip-three">
      <h4 class="tip-title">Meet with potential insurance agents:</h4>
      <p class="tip-text">Make a few appointments, bring your personal auto insurance profile with you, and ask questions. You want a fair price AND quality service. Ask about available discounts, higher deductibles, service options and claims procedures after accidents. Take notes.</p>
    </section>

    <footer class="footer">
      <div class="contact">
        <p>KPT - Silverbrook Insurance<br>Services INc.<br>4820 Larkfield Ave. Ste 210<br>Westmere CA, 91502<br>(818) 555-0142</p>
        <p>www.kpt-silverbrook.com<br>info@kpt-silverbrook.com</p>
      </div>
      <div class="follow">
        <span>FOLLOW KPT SILVERBROOK ON:</span>
        <span class="social-icon social-one" role="img" aria-label="Social network link"></span>
        <span class="social-icon social-two" role="img" aria-label="Social network link"></span>
      </div>
      <p class="footer-links"><a href="#">Join Our Newsletter</a> | <a href="#">Share this with a Friend</a> | <a href="#">Stop Future Mailings</a></p>
    </footer>
  </main>
</body>
</html>
```